Lintel Systems

Looking for a web site design to market our services/applications
We write and supply bespoke web applications for the offshore and construction industries
Our initial product is Volk - rope access equipment management
Our buyers will be Rope Access companies via trade associations such as KEFOB and GLUMP
we have a logo designed see it attached we would like to see crisp professional designs based around these colours and design
we will supply web copy later
looking for home, services, blog, contact us, order and a general template (privacy, site map, T&C) pages
Updates
This payment will be for the homepage only
We can discuss other options (pages) with the successful designer
Regards
Norman
Industry/Entity Type
Construction
Look and feel

```html
<!DOCTYPE html>
<html lang="en">
<head>
<meta charset="utf-8">
<title>Lintel Systems — Rope Access Equipment Management</title>
<link rel="stylesheet" href="https://fonts.googleapis.com/css2?family=Oswald:wght@400&family=Roboto+Condensed:wght@400;700&family=Noto+Sans:wght@400;700&display=swap">
<style>
:root{
  --navy:#27268f;
  --sky:#1ea3e0;
  --page:#f1f1f1;
  --ink:#222;
  --footer:#252525;
  --tile:#e6e6e6;
  --white:#fff;
}
*{box-sizing:border-box;margin:0;padding:0}
html,body{width:918px;height:1200px;overflow:hidden}
body{background:var(--page);font-family:"Noto Sans",sans-serif;color:var(--ink);position:relative}
.abs{position:absolute}

/* header */
.brand{left:50px;top:18px;display:flex;align-items:center;height:75px}
.brand-mark{width:52px;height:52px;border-radius:6px;background:linear-gradient(#fafafa,#dcdcdc);box-shadow:0 1px 3px rgba(0,0,0,.2)}
.brand-rule{width:1px;height:75px;background:#bbb;margin:0 8px 0 11px}
.brand-name{font-family:"Noto Sans",sans-serif;font-weight:700;font-size:19px;line-height:20px;color:var(--navy)}
.badge{left:565px;top:6px;width:31px;height:27px;border-radius:50%;background:var(--navy);color:var(--white);font:700 9px/27px "Noto Sans",sans-serif;text-align:center}
.help{left:598px;top:20px;width:183px;height:22px;background:var(--white);font:11px/22px "Noto Sans",sans-serif;text-align:center}
.help b{font-weight:700}
.social{left:788px;top:20px;display:flex;gap:4px}
.social span{height:22px;padding:0 4px;background:var(--navy);color:var(--white);font:10px/22px "Noto Sans",sans-serif}
.nav{left:470px;top:53px;width:398px;height:27px;background:var(--white);display:flex;justify-content:space-around;align-items:center;font:12px "Roboto Condensed",sans-serif;color:var(--navy)}
.nav .current{color:var(--sky)}

/* hero */
.hero{left:50px;top:104px;width:818px;height:264px;border:1px solid #ccc;
  background:linear-gradient(100deg,#1d3f7a 0%,#6d8fb8 30%,#d08a2e 45%,#2b4f86 60%,#e9e4cf 78%,#5a6b88 100%)}
.hero-caption{left:191px;top:285px;width:389px;height:49px;background:rgba(40,40,40,.8);color:var(--white);font:26px/49px "Oswald",sans-serif;padding-left:10px;letter-spacing:-.3px}
.dots{left:432px;top:377px;display:flex;gap:6px}
.dots i{width:9px;height:9px;background:#6cc8ee}
.dots i.on{background:var(--navy)}

/* features */
.feature{top:415px;width:240px;text-align:center}
.feature-icon{width:108px;height:108px;border-radius:50%;background:var(--white);margin:0 auto;display:flex;align-items:center;justify-content:center}
.feature h2{font:400 22px/26px "Oswald",sans-serif;color:var(--sky);margin-top:15px}
.feature p{font-size:11.3px;line-height:14.5px}
.btn{display:inline-block;margin-top:6px;background:var(--navy);color:var(--white);font-size:11px;line-height:22px;padding:0 10px}

/* section headings */
.section-head{left:48px;width:820px;display:flex;align-items:center;font:400 22px "Oswald",sans-serif;color:var(--navy)}
.section-head em{font-style:normal;color:var(--sky);margin-left:6px}
.section-head .hatch{flex:1;height:9px;margin-left:6px;background:repeating-linear-gradient(115deg,#777 0 1px,transparent 1px 3px)}

.laptop{left:50px;top:740px;width:256px;height:160px;border-radius:6px;background:linear-gradient(160deg,#3a3a3a 0%,#f4f4f4 40%,#c9cbcd 100%)}
.welcome{left:329px;top:725px;width:540px;font-size:10.4px;line-height:16px}
.welcome p+p{margin-top:16px}

/* clients */
.clients{left:48px;top:983px;display:flex;gap:12px}
.client{width:126px;height:87px;background:var(--tile);border:2px solid var(--white);display:flex;align-items:center;justify-content:center;gap:6px}
.client-name{font:700 16px "Noto Sans",sans-serif;color:#111}
.client-dot{width:10px;height:10px;background:#111}
.cert{width:82px;height:58px;border:3px solid #1f2f6b;border-radius:4px;background:var(--white)}

/* footer */
.footer{left:49px;top:1101px;width:819px;height:99px;background:var(--footer);color:var(--white)}
.fcol{position:absolute;top:18px;display:flex;gap:10px}
.fcol h3{font:400 13px "Oswald",sans-serif;margin-bottom:3px}
.fcol p{font-size:9.5px;line-height:15px}
.fsocial{display:flex;gap:6px;font-size:9px;margin-top:2px}
</style>
</head>
<body>

<header>
  <div class="abs brand">
    <div class="brand-mark"></div>
    <div class="brand-rule"></div>
    <div class="brand-name">Lintel<br>Systems</div>
  </div>
  <div class="abs badge">24/7</div>
  <div class="abs help"><b>Need Help?</b> Call Us &nbsp;000-000-0000</div>
  <div class="abs social"><span>Chatter</span><span>Postly</span><span>Circlr</span></div>
  <nav class="abs nav">
    <span class="current">Home</span><span>Services</span><span>Blog</span><span>Order</span><span>Privacy</span><span>Contact Us</span>
  </nav>
</header>

<div class="abs hero" role="img" aria-label="Rope access technician working at height over the sea, with a desktop monitor showing the software"></div>
<div class="abs hero-caption">ROPE ACCESS EQUIPMENT MANAGEMENT</div>
<div class="abs dots"><i></i><i class="on"></i><i></i><i></i></div>

<section>
  <div class="abs feature" style="left:45px">
    <div class="feature-icon">
      <svg width="66" height="58" viewBox="0 0 66 58" fill="none" stroke="#27268f" stroke-width="6" stroke-linejoin="round">
        <rect x="3" y="24" width="10" height="30" rx="2" fill="#27268f" stroke="none"/>
        <path d="M20 52V26l12-14 4-9c6 0 8 5 6 12l-3 9h17c4 0 6 4 4 8l-5 16c-1 3-3 4-6 4z"/>
      </svg>
    </div>
    <h2>EASY TO USE</h2>
    <p>Lorem Ipsum is simply dummy text of the printing and typesetting industry. Lorem Ipsum has been</p>
    <span class="btn">Read more</span>
  </div>
  <div class="abs feature" style="left:339px">
    <div class="feature-icon"><span style="font:700 76px/1 'Noto Sans',sans-serif;color:var(--navy)">?</span></div>
    <h2>INSTANT HELP</h2>
    <p>Lorem Ipsum is simply dummy text of the printing and typesetting industry. Lorem Ipsum has been</p>
    <span class="btn">Read more</span>
  </div>
  <div class="abs feature" style="left:632px">
    <div class="feature-icon">
      <svg width="66" height="66" viewBox="0 0 66 66">
        <g fill="#27268f" transform="translate(33 33)">
          <rect x="-7" y="-33" width="14" height="66" rx="2"/>
          <rect x="-7" y="-33" width="14" height="66" rx="2" transform="rotate(45)"/>
          <rect x="-7" y="-33" width="14" height="66" rx="2" transform="rotate(90)"/>
          <rect x="-7" y="-33" width="14" height="66" rx="2" transform="rotate(135)"/>
          <circle r="23"/>
          <circle r="10" fill="#fff"/>
        </g>
      </svg>
    </div>
    <h2>COOL SETTINGS</h2>
    <p>Lorem Ipsum is simply dummy text of the printing and typesetting industry. Lorem Ipsum has been</p>
    <span class="btn">Read more</span>
  </div>
</section>

<section>
  <h2 class="abs section-head" style="top:678px">Welcome to<em>Lintel Systems</em><span class="hatch"></span></h2>
  <div class="abs laptop" role="img" aria-label="Laptop showing a software screenshot"></div>
  <div class="abs welcome">
    <p>There are many variations of passages of Lorem Ipsum available, but the majority have suffered alteration in some form, by injected humour, or randomised words which don't look even slightly believable. If you are going to use a passage of Lorem Ipsum, you need to be sure there isn't anything embarrassing hidden in the middle of text. All the Lorem Ipsum generators on the Internet tend to repeat predefined chunks as necessary, making this the first true generator on the Internet. It uses a dictionary of over 200 Latin words, combined with a handful of model sentence structures, to generate Lorem Ipsum which looks reasonable. The generated Lorem Ipsum is therefore always free from repetition, injected humour, or non-characteristic words etc.</p>
    <p>It is a long established fact that a reader will be distracted by the readable content of a page when looking at its layout. The point of using Lorem Ipsum is that it has a more-or-less normal distribution of letters, as opposed to using.</p>
  </div>
</section>

<section>
  <h2 class="abs section-head" style="top:940px">Our<em>Clent</em><span class="hatch"></span></h2>
  <div class="abs clients">
    <div class="client"><span class="client-name">GLUMP</span><span class="client-dot"></span></div>
    <div class="client"><span class="cert"></span></div>
    <div class="client"><span class="client-name">GLUMP</span><span class="client-dot"></span></div>
    <div class="client"><span class="cert"></span></div>
    <div class="client"><span class="client-name">GLUMP</span><span class="client-dot"></span></div>
    <div class="client"><span class="cert"></span></div>
  </div>
</section>

<footer class="abs footer">
  <div class="fcol" style="left:16px">
    <svg width="20" height="28" viewBox="0 0 20 28"><path d="M10 0a9 9 0 0 0-9 9c0 7 9 19 9 19s9-12 9-19a9 9 0 0 0-9-9z" fill="#fff"/><circle cx="10" cy="9" r="3" fill="#252525"/></svg>
    <div><h3>Address</h3><p>Lorem Ipsum used since the 1500s<br>is reproduced below for those</p></div>
  </div>
  <div class="fcol" style="left:232px">
    <svg width="20" height="28" viewBox="0 0 20 28"><path d="M4 2l5 1 1 6-3 2c1 4 3 7 6 9l3-2 4 4-2 4c-9-2-16-11-17-21z" fill="#fff"/></svg>
    <div><h3>Call</h3><p><b>T -</b> 000 - 0000 - 0000<br><b>F -</b> 000 - 0000 - 0000</p></div>
  </div>
  <div class="fcol" style="left:421px">
    <svg width="36" height="22" viewBox="0 0 36 22"><rect x="1" y="1" width="34" height="20" fill="none" stroke="#fff" stroke-width="2"/><path d="M1 1l17 12L35 1M1 21l13-10M35 21L22 11" fill="none" stroke="#fff" stroke-width="2"/></svg>
    <div><h3>Contact</h3><p><b>E -</b> hello@lintelmail.com</p><div class="fsocial"><span>Chatter</span><span>Postly</span><span>Circlr</span></div></div>
  </div>
  <div class="fcol" style="left:648px;top:28px">
    <svg width="22" height="22" viewBox="0 0 22 22"><circle cx="11" cy="11" r="9.5" fill="none" stroke="#fff" stroke-width="1.6"/><path d="M14.5 8a4 4 0 1 0 0 6" fill="none" stroke="#fff" stroke-width="1.6"/></svg>
    <p>© 2014 by Lintel Systems.</p>
  </div>
</footer>

</body>
</html>
```